Banner Designs for Drone Defense Ad Campaign

Corvane is a security consulting and services company that offers a service called SkyMindful. SkyMindful helps our customers identify security risks from drones and develops comprehensive protection programs. We are looking for a designer to create a banner ad in three sizes for our campaign.
Target Market(s)
Our campaign is geared to the sports and entertainment industry, specifically large event venues and their security operation.
Industry/Entity Type
Security
Font styles to use
Other font styles liked:
- Raleway
Requirements
Must have
- Banner Objective
The visual and textual content of the banner should prompt the viewer to quickly identify the service offered and the information that is available to download.
Banner Design
Logo: SkyMindful logo
Call to Action Button in Red: Get It Here (On Right or or Upper Right)
Title in Larger Font: Guide to UAS Risk Mitigation
Subtitle in smaller Font: 5 Steps to Develop Your Comprehensive UAS Defense Program
Background: Stadium with a drone flying in foreground
Font: Raleway
Banner Sizes
1 - 1200x670 pixels
2 - 1510x196 pixels
3 - 1200x628 pixels

```html
<!DOCTYPE html>
<html lang="en">
<head>
<meta charset="utf-8">
<title>SkyMindful Banner Set</title>
<link href="https://fonts.googleapis.com/css2?family=Raleway:wght@400;500;600&display=swap" rel="stylesheet">
<style>
  :root{
    --page:#ffffff;
    --sky:#6fb4e6;
    --sky-light:#a9d3f0;
    --stands:#2a44a8;
    --stands-dark:#1c2a86;
    --pitch:#6cc03a;
    --pitch-dark:#3f8f2a;
    --band:rgba(34,40,140,0.82);
    --band-soft:rgba(34,40,140,0.72);
    --brand:#2f6fc4;
    --brand-sub:#ffffff;
    --cta-light:#ec727c;
    --cta-dark:#e20f1f;
    --text:#ffffff;
  }
  *{box-sizing:border-box;margin:0;padding:0}
  html,body{width:1067px;height:1200px;overflow:hidden;background:var(--page)}
  body{position:relative;font-family:"Raleway",sans-serif;color:var(--text)}

  .banner{position:absolute;overflow:hidden}
  .banner--large{left:133px;top:23px;width:800px;height:447px}
  .banner--medium{left:133px;top:517px;width:800px;height:419px}
  .banner--strip{left:30px;top:983px;width:1007px;height:131px}

  .scene{position:absolute;inset:0}
  .scene--stadium{
    background:linear-gradient(180deg,var(--sky-light) 0%,var(--sky) 30%,var(--stands) 50%,var(--stands-dark) 75%,var(--pitch) 92%,var(--pitch-dark) 100%);
  }
  .scene--strip{
    background:linear-gradient(100deg,var(--stands-dark) 0%,var(--stands) 25%,var(--pitch) 35%,var(--pitch-dark) 52%,var(--stands-dark) 56%,var(--stands-dark) 100%);
  }

  .brand{position:absolute;text-align:right;line-height:1}
  .brand__name{display:block;font-weight:500;color:var(--brand);font-size:37px;letter-spacing:-0.5px}
  .brand__by{display:block;font-weight:400;color:var(--brand-sub);font-size:17px;margin-top:4px}
  .banner--large .brand,.banner--medium .brand{left:292px;top:46px;width:240px}
  .banner--strip .brand{left:26px;top:46px;width:210px}
  .banner--strip .brand__name{font-size:25px}
  .banner--strip .brand__by{font-size:13px;margin-top:3px}

  .cta{position:absolute;display:flex;align-items:center;justify-content:center;
    background:linear-gradient(90deg,var(--cta-light),var(--cta-dark));
    color:var(--text);font-weight:500;text-decoration:none;letter-spacing:.5px}
  .banner--large .cta,.banner--medium .cta{left:589px;top:37px;width:176px;height:65px;font-size:22px}
  .banner--strip .cta{left:883px;top:21px;width:109px;height:39px;font-size:14px}

  .band{position:absolute;left:17px;width:766px;display:flex;align-items:center;justify-content:center;text-align:center}
  .band--title{background:var(--band)}
  .band--subtitle{background:var(--band-soft)}
  .banner--large .band--title{top:215px;height:109px}
  .banner--large .band--subtitle{top:343px;height:73px}
  .banner--medium .band--title{top:190px;height:107px}
  .banner--medium .band--subtitle{top:316px;height:73px}

  .title{font-weight:600;font-size:50px;letter-spacing:.3px}
  .subtitle{font-weight:600;font-size:22px;letter-spacing:.2px}

  .strip-copy{position:absolute;left:500px;top:2px;width:395px;text-align:center;line-height:1.1}
  .strip-copy .title{font-size:32px;display:block;line-height:1.22}
  .strip-copy .subtitle{font-size:19.5px;display:block;margin-top:2px;line-height:1.2}
</style>
</head>
<body>

<section class="banner banner--large">
  <div class="scene scene--stadium" role="img" aria-label="Photo of a white quadcopter drone flying above a large football stadium with blue seating and green pitch"></div>
  <div class="brand"><span class="brand__name">SkyMindful</span><span class="brand__by">By Corvane</span></div>
  <a class="cta" href="#">Get It Here</a>
  <div class="band band--title"><h1 class="title">Guide to UAS Risk Mitigation</h1></div>
  <div class="band band--subtitle"><p class="subtitle">5 Steps to Develop Your Comprehensive UAS Defense Program</p></div>
</section>

<section class="banner banner--medium">
  <div class="scene scene--stadium" role="img" aria-label="Photo of a white quadcopter drone flying above a large football stadium with blue seating and green pitch"></div>
  <div class="brand"><span class="brand__name">SkyMindful</span><span class="brand__by">By Corvane</span></div>
  <a class="cta" href="#">Get It Here</a>
  <div class="band band--title"><h2 class="title">Guide to UAS Risk Mitigation</h2></div>
  <div class="band band--subtitle"><p class="subtitle">5 Steps to Develop Your Comprehensive UAS Defense Program</p></div>
</section>

<section class="banner banner--strip">
  <div class="scene scene--strip" role="img" aria-label="Photo of a drone hovering over a stadium pitch, framed by blue-tinted stands"></div>
  <div class="brand"><span class="brand__name">SkyMindful</span><span class="brand__by">By Corvane</span></div>
  <div class="strip-copy">
    <h2 class="title">Guide to<br>UAS Risk Mitigation</h2>
    <p class="subtitle">5 Steps to Develop Your Comprehensive<br>UAS Defense Program</p>
  </div>
  <a class="cta" href="#">Get It Here</a>
</section>

</body>
</html>
```